KIVO Cosmetics LABELS

one good design wanted for the KIVO COSMETICS brand.

These are cosmetics and detergents. The labels should be about 3" wide and 4" deep. It must be colorful and interesting with some art on it. Flowers, girl, ? anything.

The word KIVO should guide your thinking a little.

It has to be bold and with striking colors. The attached images are there only as a guide of images we like and the logos are there, so you can see what we have already.

Ask any further questions please.

This design should be colorful and not finicky

Reason: Ready to work with any designer - through Brief Harbor - for other projects.

some intriguing graphics, images or something 'wow' is wanted in the designs

Those wanting something different and economic.

Cosmetics

• Each label in a range is to be the same 'ish and to allow space for the name of the individual product to be added; such as Seaweed Shampoo.

Use of the logo will be all labels but small in a corner, or ...

USE OF THE SHOWN IMAGES, SHOULD BE THERE BUT NOT PROMINENTLY

```html
<!DOCTYPE html>
<html lang="en">
<head>
<meta charset="utf-8">
<title>KIVO Cosmetics – Seaweed Shampoo Label</title>
<link rel="stylesheet" href="https://fonts.googleapis.com/css2?family=League+Gothic&family=Josefin+Sans:wght@300;700&display=swap">
<style>
  :root {
    --magenta: #9e1f6e;
    --ink: #231f20;
    --yellow: #fff200;
    --brand-red: #e8202a;
    --skin-light: #f6e0cf;
    --skin-mid: #e9c8b2;
  }
  html, body {
    margin: 0;
    padding: 0;
    overflow: hidden;
    background: #ffffff;
  }
  .label {
    position: relative;
    width: 900px;
    height: 1200px;
    overflow: hidden;
    background: var(--magenta);
    font-family: "Josefin Sans", sans-serif;
  }
  .backdrop {
    position: absolute;
    inset: 0;
  }
  .brand-word {
    font-family: "League Gothic", "Oswald", sans-serif;
    fill: var(--magenta);
  }
  .hand-visual {
    position: absolute;
    left: 52px;
    top: 170px;
    width: 495px;
    height: 700px;
  }
  .product-name {
    position: absolute;
    right: 175px;
    top: 893px;
    margin: 0;
    color: var(--yellow);
    font-weight: 300;
    font-size: 58px;
    line-height: 0.98;
    letter-spacing: -1px;
    text-align: right;
    text-transform: uppercase;
  }
  .description-band {
    position: absolute;
    left: 420px;
    top: 1010px;
    width: 325px;
    height: 44px;
    background: var(--yellow);
    color: var(--ink);
    font-weight: 300;
    font-size: 27px;
    line-height: 48px;
    text-align: right;
    box-sizing: border-box;
    padding-right: 18px;
  }
  .description-line {
    position: absolute;
    right: 175px;
    top: 1072px;
    color: var(--yellow);
    font-weight: 300;
    font-size: 22px;
    letter-spacing: 0.3px;
  }
  .brand-mark {
    position: absolute;
    right: 175px;
    top: 1118px;
    color: var(--brand-red);
    font-weight: 700;
    font-size: 30px;
    line-height: 1;
    letter-spacing: -0.5px;
  }
</style>
</head>
<body>
  <main class="label">
    <svg class="backdrop" width="900" height="1200" viewBox="0 0 900 1200" aria-hidden="true">
      <rect class="dark-panel" x="85" y="0" width="750" height="1200" fill="var(--ink)"/>
      <text class="brand-word" x="-40" y="1330" font-size="1560"
            textLength="1010" lengthAdjust="spacingAndGlyphs">KIVO</text>
    </svg>

    <svg class="hand-visual" viewBox="0 0 495 700" role="img"
         aria-label="Photograph of a hand with red painted nails gripping the large lettering">
      <defs>
        <linearGradient id="skinTone" x1="0" y1="0" x2="1" y2="1">
          <stop offset="0" stop-color="var(--skin-light)"/>
          <stop offset="1" stop-color="var(--skin-mid)"/>
        </linearGradient>
      </defs>
      <rect x="0" y="0" width="495" height="700" rx="90" fill="url(#skinTone)"/>
    </svg>

    <h1 class="product-name">Seaweed<br>Shampoo</h1>
    <div class="description-band">DESCRIPTION</div>
    <div class="description-line">DESCRIPTION</div>
    <div class="brand-mark">KIVO Cosmetics</div>
  </main>
</body>
</html>
```